Professional business cards for real estate development company

I need business cards for my new real estate development company. The company, "KORVA" is a real estate development, investment, and advisory firm with a focus on multifamily, office, and mixed-use projects across primary and secondary markets in the Southeast United States.

Style preference is modern

Industry/Entity Type

Real Estate Development

Contact Information for Business Card

The business cards need to include:
Name
Title
Mailing Address
Phone Number
Web Address

Logo is attached. I would like white to be the primary color with incorporation of the company colors: #232D3A and #B5A451

Font styles to use
Other font styles liked:
• Montserrat, Avenir

Requirements
Must have
• Company Logo. No need to include the company name since the name is in the logo.
Should not have
• No line type designs

```html
<!DOCTYPE html>
<html lang="en">
<head>
<meta charset="utf-8">
<title>KORVA — Business Card</title>
<link href="https://fonts.googleapis.com/css2?family=Montserrat:wght@500;600&family=Open+Sans:wght@400;600&display=swap" rel="stylesheet">
<style>
  :root {
    --navy: #232D3A;
    --gold: #B5A451;
    --white: #FFFFFF;
    --ink: #4a4f57;
    --page: #FFFFFF;
  }
  html, body {
    margin: 0;
    padding: 0;
    width: 1200px;
    height: 1118px;
    overflow: hidden;
    background: var(--page);
  }
  .card {
    position: absolute;
    left: 357px;
    top: 360px;
    width: 491px;
    height: 315px;
    background: var(--white);
    overflow: hidden;
    font-family: "Open Sans", sans-serif;
  }
  .card-shapes {
    position: absolute;
    inset: 0;
    width: 491px;
    height: 315px;
  }
  .brand {
    position: absolute;
    left: 30px;
    top: 80px;
    display: flex;
    align-items: center;
    gap: 10px;
  }
  .brand-mark {
    width: 14px;
    height: 14px;
    background: var(--navy);
  }
  .brand-name {
    font-family: "Montserrat", sans-serif;
    font-weight: 600;
    font-size: 34px;
    letter-spacing: 2px;
    color: var(--navy);
    line-height: 1;
  }
  .person {
    position: absolute;
    right: 24px;
    top: 71px;
    text-align: right;
  }
  .person-name {
    font-family: "Open Sans", sans-serif;
    font-weight: 600;
    font-size: 18px;
    color: var(--gold);
    letter-spacing: 0.5px;
    line-height: 1.2;
  }
  .person-title {
    font-size: 12px;
    color: var(--white);
    letter-spacing: 2.4px;
    margin-top: 3px;
  }
  .contact-list {
    position: absolute;
    margin: 0;
    padding: 0;
    list-style: none;
    font-size: 15px;
    color: var(--ink);
  }
  .contact-list li {
    display: flex;
    align-items: center;
    height: 22px;
    gap: 12px;
  }
  .contact-list svg {
    width: 13px;
    height: 13px;
    fill: var(--gold);
    flex: none;
  }
  .contact-phones {
    left: 24px;
    top: 230px;
    font-size: 14px;
    letter-spacing: 0.5px;
  }
  .contact-details {
    right: 18px;
    top: 205px;
  }
  .contact-details li {
    justify-content: flex-end;
  }
</style>
</head>
<body>
  <article class="card" aria-label="KORVA business card">
    <svg class="card-shapes" viewBox="0 0 327 210" preserveAspectRatio="none" aria-hidden="true">
      <rect class="top-band" x="0" y="0" width="110" height="20" fill="var(--navy)"/>
      <polygon class="header-block" points="132,0 327,0 327,90 202,90 187,132" fill="var(--navy)"/>
      <polygon class="gold-sash" points="107,0 132,0 187,132 162,130" fill="var(--gold)"/>
      <polygon class="footer-gold" points="0,185 135,185 147,210 0,210" fill="var(--gold)"/>
      <polygon class="footer-navy" points="135,185 327,185 327,210 147,210" fill="var(--navy)"/>
    </svg>

    <div class="brand">
      <span class="brand-mark" aria-hidden="true"></span>
      <span class="brand-name">KORVA</span>
    </div>

    <div class="person">
      <div class="person-name">PERSONS NAME</div>
      <div class="person-title">PERSONS TITLE</div>
    </div>

    <ul class="contact-list contact-phones">
      <li>
        <svg viewBox="0 0 24 24" aria-hidden="true"><path d="M6.6 10.8a15.2 15.2 0 0 0 6.6 6.6l2.2-2.2a1 1 0 0 1 1-.25 11.4 11.4 0 0 0 3.6.57 1 1 0 0 1 1 1V20a1 1 0 0 1-1 1A17 17 0 0 1 3 4a1 1 0 0 1 1-1h3.5a1 1 0 0 1 1 1c0 1.25.2 2.45.57 3.6a1 1 0 0 1-.25 1z"/></svg>
        <span>(999) 222-5555</span>
      </li>
      <li>
        <svg viewBox="0 0 24 24" aria-hidden="true"><path d="M7 1h10a2 2 0 0 1 2 2v18a2 2 0 0 1-2 2H7a2 2 0 0 1-2-2V3a2 2 0 0 1 2-2zm0 3v14h10V4z"/></svg>
        <span>(999) 222-4444</span>
      </li>
    </ul>

    <ul class="contact-list contact-details">
      <li>
        <span>aaaaaaa@nnn.com</span>
        <svg viewBox="0 0 24 24" aria-hidden="true"><path d="M2 5h20v14H2z"/></svg>
      </li>
      <li>
        <span>City, State Name, 77</span>
        <svg viewBox="0 0 24 24" aria-hidden="true"><path d="M12 1a8 8 0 0 0-8 8c0 6 8 14 8 14s8-8 8-14a8 8 0 0 0-8-8zm0 11a3 3 0 1 1 0-6 3 3 0 0 1 0 6z"/></svg>
      </li>
      <li>
        <span>www.sssssssss.com</span>
        <svg viewBox="0 0 24 24" aria-hidden="true"><path d="M12 2a10 10 0 1 0 0 20 10 10 0 0 0 0-20zm-1 2.1V11H7.1A12 12 0 0 1 11 4.1zm2 0A12 12 0 0 1 16.9 11H13zM4.1 13H11v6.9A8 8 0 0 1 4.1 13zM13 19.9V13h6.9A8 8 0 0 1 13 19.9zM4.1 11A8 8 0 0 1 9 4.5 14 14 0 0 0 5.1 11z"/></svg>
      </li>
    </ul>
  </article>
</body>
</html>
```